Redesign trade show stand graphics for Harbourline Panels

Update existing graphics of a trade show stand consisting of 2 walls. See the current design attached.

Left wall size is 2.4m high x 2700mm wide (made up of 3 pieces of 2400mm high x 900mm wide). The artwork will be printed on self adhesive stickers to cover the 2 walls.

NEW DESIGN LEFT WALL (2.4m high x 3m wide)
Headline at the top of the wall should read:
RENOVATE YOUR KITCHEN
the quick, easy and cost effective way:
JUST REPLACE THE DOORS and panels
• Cost effective: Save $$$
• Quick: approx. 15 working days
• Easy: No mess or inconvenience
• Polyurethane finish, unlimited choice of colours
• Measure, quote and install - DIY or contact our installers
• Delivery Australia wide
Harbourline Panels logo at top of left and right walls. See logo attached. “Australian made” logo somewhere on the wall (logo attached)
The main body of the left wall will contain a “before” and “after” photo of a kitchen. Size of “before” shot approximately 250mm wide x 150mm high and “after” shot approximately 1m wide x 600mm high. Photo with higher resolution will be supplied.
Text:
• We replace doors, panels, drawer fronts and kickboards - all painted in polyurethane.
• We drill doors for new or existing hinges. We supply Vorn soft closing hinges, door handles, wardrobe door tracks and decorative items such as corbels, flutes and rosettes and capping.
• Our installers measure, quote and install or save money and do it yourself - DIY
Headline under the above: UPDATE YOUR BUILT IN WARDROBES WITH NEW DOORS
Sub headline: Custom made to your sizes and painted in polyurethane in the colour of your choice
2 photos of wardrobes to go under this headline

NEW DESIGN RIGHT WALL (2.4m high x 2800mm wide made up of 1 x 1000mm piece and 2 x 900mm pieces)
Visit our website: harbourlinepanels.com.au
Headline: SAVE TIME AND MONEY – REPLACE YOUR OLD DOORS (and panels)
Sub headline: WITH ONES PAINTED IN POLYURETHANE
Sub sub headline:
TO GET A QUOTE:
• DIY measure doors and panels and fill in our Quote Form or
• Contact our installers to measure, quote and install

At 1.5m high: 2 rows of 7 rectangular outlines 400mm high x 300mm wide (for sample doors that will be hung on the wall).
Directly under that, another headline:
Many more designs in our showroom at
47 Kestrel Avenue, Marlow Heights NSW 2837
Phone: (02) 9318 6072
Email: sales@harbourlinepanels.com.au
Website: harbourlinepanels.com.au
Place image of our showroom (attached) to the left or right.

“Australian made” logo and "Trade and public welcome" logo somewhere on the wall (logos attached).
Small listing of approximately A5 size of “What we do”, “What we don’t do” and “What you do”. These will be supplied in bullet points.
Another image to use is uploaded below.

Target Market(s)

Home owners, home renovators

Industry/Entity Type

Trade

Font styles to use
Sans Serif
Other font styles liked:
• A font similar to that used on our website www.harbourlinepanels.com.au

Colors
f8972e

Requirements
Must have
• The background colour of the stand artwork should remain the same bright colour of our logo. The fonts should be similar to that used on our website www.harbourlinepanels.com.au
Nice to have
• Fun and engaging design

```html
<!DOCTYPE html>
<html lang="en">
<head>
<meta charset="utf-8">
<title>Harbourline Panels – Trade Show Walls</title>
<link rel="stylesheet" href="https://fonts.googleapis.com/css2?family=Bebas+Neue&family=Archivo+Black&family=Open+Sans:ital,wght@0,400;0,700;0,800;1,700;1,800&display=swap">
<style>
:root{
  --stage:#8b8989;
  --orange:#fdbc5c;
  --brand:#f8972e;
  --yellow:#f6e51f;
  --charcoal:#404042;
  --ink:#3a3a3c;
  --white:#ffffff;
  --red:#d9262a;
  --cell-line:#5a5a5c;
}
*{box-sizing:border-box;margin:0;padding:0}
html,body{width:787px;height:1200px;overflow:hidden}
body{background:var(--stage);position:relative;font-family:"Open Sans",Arial,sans-serif;color:var(--ink)}
.abs{position:absolute}
.condensed{font-family:"Bebas Neue","Arial Narrow",sans-serif;font-weight:400}

/* LEFT WALL */
.wall-left{left:66px;top:44px;width:655px;height:523px;background:var(--white);overflow:hidden}
.wall-left .top-band{left:0;top:0;width:655px;height:156px;background:var(--orange)}
.headline{left:0;width:100%;text-align:center;color:var(--ink);line-height:1}
.wall-left .headline{top:16px;font-size:69px}
.tagline{left:0;top:83px;width:100%;text-align:center;color:var(--white);font-weight:800;font-size:15.5px;letter-spacing:.2px}
.ribbon{background:var(--yellow);clip-path:polygon(0 0,100% 0,97% 50%,100% 100%,0 100%,3% 50%);text-align:center;color:var(--ink);line-height:1}
.wall-left .ribbon{left:47px;top:106px;width:520px;height:38px;font-size:31px;padding-top:5px}

.feature-band{left:0;top:156px;width:655px;height:170px;background:var(--charcoal)}
.after-photo{left:421px;top:156px;width:234px;height:170px;background:linear-gradient(160deg,#efeeea 0%,#d8d6d1 55%,#8a3a2a 62%,#e8e6e2 70%,#cfcdc8 100%)}
.tag{background:var(--yellow);color:var(--ink);font-weight:800;font-size:10px;text-align:center;line-height:17px}
.after-tag{left:556px;top:159px;width:66px;height:17px}
.before-frame{left:289px;top:191px;width:120px;height:110px;background:var(--white);padding:5px;box-shadow:0 3px 6px rgba(0,0,0,.4)}
.before-photo{width:100%;height:100%;background:linear-gradient(170deg,#d8c8a8 0%,#c69256 40%,#9a5a24 100%)}
.before-tag{left:299px;top:193px;width:50px;height:14px;line-height:14px;font-size:9px}

.benefits{left:42px;top:168px;list-style:none}
.benefits li{position:relative;padding-left:17px;font-style:italic;font-weight:800}
.benefits li svg{position:absolute;left:0}
.benefits .key{color:var(--yellow);font-size:13.5px;line-height:19.5px}
.benefits .key svg{top:5px}
.benefits .minor{color:var(--white);font-size:11px;line-height:12.5px;margin-top:8px}
.benefits .minor svg{top:1px}
.benefits .key + .minor{margin-top:10px}

.brand-mark{text-align:center;font-weight:800;color:var(--ink);white-space:nowrap}
.brand-mark .dot{display:block;margin:0 auto;background:var(--brand)}
.brand-left{left:24px;top:344px;width:96px;font-size:13px;line-height:15px}
.brand-left .dot{width:50px;height:50px;margin-bottom:10px}
.services{left:134px;top:338px;width:230px;list-style:none}
.services li{position:relative;padding-left:10px;font-weight:700;font-size:9.4px;line-height:10.6px;margin-bottom:7px;color:var(--ink)}
.services li::before{content:"";position:absolute;left:0;top:2px;border-left:5px solid var(--red);border-top:3.5px solid transparent;border-bottom:3.5px solid transparent}
.made-badge{left:262px;top:455px;width:96px;height:27px;background:#f2b35a;border-radius:3px;opacity:.6}
.url-bar{left:35px;top:490px;width:319px;height:19px;background:var(--orange);text-align:center;font-weight:800;font-size:11.5px;line-height:19px;color:var(--ink)}

.wardrobe-box{left:379px;top:338px;width:251px;height:169px;background:var(--orange)}
.wardrobe-box h2{position:absolute;left:13px;top:11px;color:var(--white);font-size:21px;line-height:20px}
.wardrobe-box p{position:absolute;left:13px;top:63px;width:78px;font-weight:700;font-size:10.5px;line-height:13.2px;color:var(--ink)}
.wardrobe-frame{left:96px;top:58px;width:143px;height:101px;background:var(--white);padding:4px;box-shadow:0 2px 5px rgba(0,0,0,.3)}
.wardrobe-photo{width:100%;height:100%;background:linear-gradient(90deg,#f4f3ef 0%,#e4e2dc 60%,#5a4a5a 80%,#efe9dc 100%)}

/* RIGHT WALL */
.wall-right{left:94px;top:620px;width:611px;height:524px;background:var(--white);overflow:hidden}
.wall-right .top-band{left:0;top:0;width:611px;height:103px;background:var(--orange)}
.wall-right .headline{left:0;top:16px;width:588px;font-family:"Archivo Black","Arial Black",sans-serif;font-size:29px;letter-spacing:.3px}
.wall-right .ribbon{left:86px;top:50px;width:438px;height:33px;font-size:27px;padding-top:4px}
.sub-tagline{left:0;top:86px;width:588px;text-align:center;color:var(--white);font-weight:800;font-size:9.6px}
.brand-right{left:535px;top:10px;width:72px;font-size:11px;line-height:13px}
.brand-right .dot{width:32px;height:32px;margin-bottom:6px}

.sample-wall{left:0;top:103px;width:611px;height:189px;background:var(--charcoal)}
.sample-grid{position:absolute;left:77px;top:10px;display:grid;grid-template-columns:repeat(7,61px);grid-template-rows:repeat(2,81px);column-gap:8px;row-gap:8px}
.sample-grid span{border:1px solid var(--cell-line)}

.info-band{left:0;top:292px;width:611px;height:148px;background:var(--orange)}
.visit{left:0;top:303px;width:622px;text-align:center;font-weight:700;font-size:16.5px;color:var(--ink)}
.showroom-frame{left:37px;top:338px;width:265px;height:159px;background:var(--white);padding:4px;box-shadow:0 6px 10px rgba(0,0,0,.35)}
.showroom-photo{width:100%;height:100%;background:linear-gradient(180deg,#e9e8e4 0%,#f5f5f2 60%,#7d7f86 75%,#6f7178 100%)}
.steps-tab{left:319px;top:339px;width:224px;height:14px;background:var(--red);color:var(--white);font-weight:800;font-size:9px;line-height:14px;padding-left:8px;clip-path:polygon(0 0,100% 0,97% 50%,100% 100%,0 100%)}
.step{position:absolute;display:flex;align-items:flex-start;gap:3px}
.step svg{flex:none}
.step b{flex:none;color:var(--red);font-size:13px;line-height:13px;font-weight:800}
.step p{flex:1;font-weight:700;font-size:6.8px;line-height:8px;color:var(--ink)}
.step-1{left:323px;top:358px;width:122px}
.step-2{left:323px;top:393px;width:122px}
.step-3{left:449px;top:357px;width:156px}
.step-4{left:449px;top:398px;width:156px}

.contact{left:321px;top:446px;width:205px;white-space:nowrap}
.contact h3{font-weight:800;font-size:12.5px;line-height:15px;color:#555}
.contact .addr{font-size:9px;line-height:12px}
.contact .phone{font-weight:800;font-size:15px;line-height:19px;color:var(--brand);margin-top:2px}
.contact .email{font-size:9px;line-height:12px}
.welcome-badge{left:528px;top:443px;width:60px;height:60px;border-radius:50%;background:var(--brand)}
</style>
</head>
<body>

<section class="abs wall-left" aria-label="Left wall artwork">
  <div class="abs top-band"></div>
  <h1 class="abs headline condensed">RENOVATE YOUR KITCHEN</h1>
  <p class="abs tagline">THE QUICK, EASY AND COST EFFECTIVE WAY</p>
  <div class="abs ribbon condensed">JUST REPLACE THE DOORS AND PANELS</div>

  <div class="abs feature-band"></div>
  <div class="abs after-photo" role="img" aria-label="Photo of a renovated kitchen with white doors, after"></div>
  <div class="abs tag after-tag">AFTER</div>
  <div class="abs before-frame"><div class="before-photo" role="img" aria-label="Photo of the old timber kitchen, before"></div></div>
  <div class="abs tag before-tag">BEFORE</div>

  <ul class="abs benefits">
    <li class="key"><svg width="12" height="10" viewBox="0 0 12 10"><path d="M1 5l3.5 3.5L11 1" fill="none" stroke="#f6e51f" stroke-width="2.4"/></svg>Cost effective: Save $$$</li>
    <li class="key"><svg width="12" height="10" viewBox="0 0 12 10"><path d="M1 5l3.5 3.5L11 1" fill="none" stroke="#f6e51f" stroke-width="2.4"/></svg>Quick: approx. 15 working days</li>
    <li class="key"><svg width="12" height="10" viewBox="0 0 12 10"><path d="M1 5l3.5 3.5L11 1" fill="none" stroke="#f6e51f" stroke-width="2.4"/></svg>Easy: No mess or inconvenience</li>
    <li class="minor"><svg width="12" height="10" viewBox="0 0 12 10"><path d="M1 5l3.5 3.5L11 1" fill="none" stroke="#f6e51f" stroke-width="2.4"/></svg>Polyurethane finish, unlimited<br>choice of colours</li>
    <li class="minor"><svg width="12" height="10" viewBox="0 0 12 10"><path d="M1 5l3.5 3.5L11 1" fill="none" stroke="#f6e51f" stroke-width="2.4"/></svg>DIY or contact an installer to<br>measure, quote and install</li>
    <li class="minor"><svg width="12" height="10" viewBox="0 0 12 10"><path d="M1 5l3.5 3.5L11 1" fill="none" stroke="#f6e51f" stroke-width="2.4"/></svg>Delivery Australia wide</li>
  </ul>

  <div class="abs brand-mark brand-left"><span class="dot"></span>Harbourline<br>Panels</div>
  <ul class="abs services">
    <li>Custom made doors, panels, drawer fronts and kickboards painted in polyurethane finish.</li>
    <li>Doors drilled for new or existing hinges.</li>
    <li>Supply of Vorn soft closing or standard hinges, door handles, wardrobe door tracks and decorative items such as corbels, flutes, rosettes and capping.</li>
    <li>Showroom at 47 Kestrel Avenue, Marlow Heights NSW 2837</li>
  </ul>
  <div class="abs made-badge" aria-hidden="true"></div>
  <div class="abs url-bar">WWW.HARBOURLINEPANELS.COM.AU</div>

  <div class="abs wardrobe-box">
    <h2 class="condensed">UPDATE YOUR BUILT IN<br>WARDROBES WITH NEW DOORS</h2>
    <p>Custom made to your sizes and painted in polyurethane in the colour of your choice</p>
    <div class="abs wardrobe-frame"><div class="wardrobe-photo" role="img" aria-label="Photo of a bedroom with white built-in wardrobe doors"></div></div>
  </div>
</section>

<section class="abs wall-right" aria-label="Right wall artwork">
  <div class="abs top-band"></div>
  <h1 class="abs headline">SAVE TIME AND MONEY</h1>
  <div class="abs ribbon condensed">REPLACE YOUR OLD DOORS &amp; PANELS</div>
  <p class="abs sub-tagline">WITH NEW CUSTOM MADE ONES PAINTED IN POLYURETHANE FINISH</p>
  <div class="abs brand-mark brand-right"><span class="dot"></span>Harbourline<br>Panels</div>

  <div class="abs sample-wall">
    <div class="sample-grid" aria-label="Spaces for sample doors">
      <span></span><span></span><span></span><span></span><span></span><span></span><span></span>
      <span></span><span></span><span></span><span></span><span></span><span></span><span></span>
    </div>
  </div>

  <div class="abs info-band"></div>
  <p class="abs visit">Visit our website: harbourlinepanels.com.au</p>
  <div class="abs showroom-frame"><div class="showroom-photo" role="img" aria-label="Photo of the showroom with white sample doors on display"></div></div>

  <div class="abs steps-tab">HOW TO GET A QUOTE OR PLACE AN ORDER</div>
  <div class="step step-1">
    <svg width="22" height="22" viewBox="0 0 22 22"><path d="M3 19L17 5l2 2L5 21H3z" fill="none" stroke="#3a3a3c" stroke-width="1.8"/><path d="M4 4h6M4 4v6" stroke="#3a3a3c" stroke-width="1.8"/></svg>
    <b>1</b><p>Choose your door design, edges, colour, finish and accessories.</p>
  </div>
  <div class="step step-2">
    <svg width="22" height="16" viewBox="0 0 22 16"><rect x="1" y="2" width="20" height="13" fill="#3a3a3c"/><path d="M1 2l10 7 10-7" fill="none" stroke="#fdbc5c" stroke-width="1.4"/></svg>
    <b>2</b><p>DIY or get an installer to measure your doors and panels and fill in a quote form.</p>
  </div>
  <div class="step step-3">
    <svg width="24" height="24" viewBox="0 0 24 24"><circle cx="10" cy="10" r="8" fill="#3a3a3c"/><text x="10" y="14" font-size="11" font-weight="800" fill="#fdbc5c" text-anchor="middle" font-family="Open Sans,sans-serif">$</text><rect x="14" y="16" width="9" height="6" fill="#3a3a3c"/></svg>
    <b>3</b><p>On receipt of our quote, pay 50% deposit to order your doors. If using an installer, they will quote the installation.</p>
  </div>
  <div class="step step-4">
    <svg width="24" height="16" viewBox="0 0 24 16"><rect x="1" y="2" width="14" height="9" fill="#3a3a3c"/><path d="M15 5h5l3 4v2h-8z" fill="#3a3a3c"/><circle cx="5" cy="13" r="2.2" fill="#3a3a3c"/><circle cx="19" cy="13" r="2.2" fill="#3a3a3c"/></svg>
    <b>4</b><p>Your doors will be ready for delivery or pick up in approx. 15 working days.</p>
  </div>

  <div class="abs contact">
    <h3>More designs in our showroom</h3>
    <p class="addr">47 Kestrel Avenue, Marlow Heights NSW 2837</p>
    <p class="phone">Phone: (02) 9318 6072</p>
    <p class="email">Email: sales@harbourlinepanels.com.au</p>
  </div>
  <div class="abs welcome-badge" aria-hidden="true"></div>
</section>

</body>
</html>
```